Marnie Lux Business Card Design

I need a business card for my daughter. She has it all described in the file below. But it needs to be square in shape. http://www.marnielux.com is her web site

Target Market(s)

18-35 year old women

Industry/Entity Type

Fashion

Contact Information for Business Card

Please look at the attached file as it has all the details.

Requirements
Must have
• Please look at the attached file as it has all the details.
Nice to have
Should not have

```html
<!DOCTYPE html>
<html lang="en">
<head>
<meta charset="utf-8">
<title>Marnie Lux Business Card</title>
<link rel="stylesheet" href="https://fonts.googleapis.com/css2?family=Abril+Fatface&family=Cormorant+Garamond:wght@500&family=Dancing+Script:wght@500&display=swap">
<style>
  :root {
    --backdrop: #ececec;
    --ink: #0d0d0d;
    --blush: #fbdce3;
    --paper: #ffffff;
    --marble-light: #ebe6e3;
    --marble-dark: #161616;
  }
  * { margin: 0; padding: 0; box-sizing: border-box; }
  html, body { width: 1200px; height: 1000px; overflow: hidden; }
  body { background: var(--backdrop); position: relative; }

  .card { position: absolute; top: 40px; width: 490px; height: 489px; }

  /* Front */
  .card-front { left: 81px; overflow: hidden; }
  .marble { position: absolute; inset: 0; width: 100%; height: 100%; }
  .name-panel {
    position: absolute; left: 46px; top: 151px; width: 398px; height: 187px;
    background: var(--blush); text-align: center;
  }
  .brand-name {
    font-family: "Abril Fatface", serif; font-size: 46px; letter-spacing: 2px;
    color: var(--ink); margin-top: 38px; line-height: 1;
  }
  .brand-rule {
    width: 282px; height: 2px; background: var(--paper); margin: 13px auto 0;
  }
  .brand-tagline {
    font-family: "Dancing Script", cursive; font-size: 32px; color: var(--ink);
    margin-top: 2px;
  }

  /* Back */
  .card-back { left: 630px; background: var(--ink); padding: 18px; }
  .back-panel { width: 100%; height: 100%; background: var(--blush); position: relative; }
  .role-bar {
    position: absolute; left: 25px; top: 19px; width: 402px; height: 55px;
    background: var(--ink); color: var(--paper);
    font-family: "Dancing Script", cursive; font-size: 21px; font-style: italic;
    display: flex; align-items: center; justify-content: center; white-space: nowrap;
  }
  .contact-list { position: absolute; left: 55px; top: 94px; list-style: none; }
  .contact-item {
    display: flex; align-items: center; height: 60px;
    font-family: "Cormorant Garamond", serif; font-weight: 500; font-size: 27px; color: var(--ink);
  }
  .contact-icon { width: 40px; height: 40px; margin-right: 20px; flex: none; }
</style>
</head>
<body>

<section class="card card-front">
  <svg class="marble" viewBox="0 0 490 489" role="img" aria-label="Black and white veined marble background split diagonally">
    <defs>
      <linearGradient id="lightStone" x1="0" y1="0" x2="1" y2="1">
        <stop offset="0" stop-color="#dcd7d4"/>
        <stop offset="1" stop-color="var(--marble-light)"/>
      </linearGradient>
      <linearGradient id="darkStone" x1="0" y1="0" x2="1" y2="1">
        <stop offset="0" stop-color="#0a0a0a"/>
        <stop offset="1" stop-color="#262626"/>
      </linearGradient>
    </defs>
    <rect width="490" height="489" fill="url(#lightStone)"/>
    <polygon points="40,0 490,0 490,489" fill="url(#darkStone)"/>
  </svg>
  <div class="name-panel">
    <h1 class="brand-name">MARNIE LUX</h1>
    <div class="brand-rule"></div>
    <p class="brand-tagline">fluent in fashion</p>
  </div>
</section>

<section class="card card-back">
  <div class="back-panel">
    <div class="role-bar">blogger &amp; youtuber // beauty - fashion - travel</div>
    <ul class="contact-list">
      <li class="contact-item">
        <svg class="contact-icon" viewBox="0 0 40 40"><circle cx="20" cy="20" r="20" fill="var(--ink)"/></svg>
        photoloop.com/marnieluxxo
      </li>
      <li class="contact-item">
        <svg class="contact-icon" viewBox="0 0 40 40"><circle cx="20" cy="20" r="20" fill="var(--ink)"/></svg>
        chirpline.com/marnieluxxo
      </li>
      <li class="contact-item">
        <svg class="contact-icon" viewBox="0 0 40 40"><circle cx="20" cy="20" r="20" fill="var(--ink)"/></svg>
        @marnieluxxo
      </li>
      <li class="contact-item">
        <svg class="contact-icon" viewBox="0 0 40 40">
          <circle cx="20" cy="20" r="20" fill="var(--ink)"/>
          <rect x="10" y="13" width="20" height="14" fill="none" stroke="var(--paper)" stroke-width="2"/>
          <polyline points="10,13 20,21 30,13" fill="none" stroke="var(--paper)" stroke-width="2"/>
        </svg>
        marnie@marnielux.com
      </li>
      <li class="contact-item">
        <svg class="contact-icon" viewBox="0 0 40 40">
          <circle cx="20" cy="20" r="20" fill="var(--ink)"/>
          <circle cx="20" cy="20" r="11" fill="none" stroke="var(--paper)" stroke-width="2"/>
          <ellipse cx="20" cy="20" rx="5" ry="11" fill="none" stroke="var(--paper)" stroke-width="1.5"/>
          <line x1="9" y1="20" x2="31" y2="20" stroke="var(--paper)" stroke-width="1.5"/>
        </svg>
        marnielux.com
      </li>
      <li class="contact-item">
        <svg class="contact-icon" viewBox="0 0 40 40"><circle cx="20" cy="20" r="20" fill="var(--ink)"/></svg>
        viewstream.com/marnielux
      </li>
    </ul>
  </div>
</section>

</body>
</html>
```